Packaging for Hair Fibers Product

We are a start up company looking for a new packaging design for hair building fibers. These are aimed at predominantly men but also women as well. We already have a logo and i have the packaging design from our competitors. We are wanting to keep the look masculine as 90% of our users will be middle aged men. We would like the colours to be black and white but are open to other colours as well.
It will need to have our logo and the following somewhere on the front.
"Instant Fuller & Thicker Hair" & "Natural Hair Building Fibers" "28g" or "Net Weight 28g"
We only need the front of the packaging designed, please make the other sides of the packaging the same colour but blank.
Target Market(s)
Men 25+
Industry/Entity Type
Hair And Beauty
Requirements
Must have
- Logo which i have included. and the following somewhere on the front.
- "Instant Fuller & Thicker Hair" ; "Natural Hair Building Fibers" "28g" or "Net Weight 28g"
Nice to have
- Make it stand out from the competition or similar to the brantiq example.

```html
<!DOCTYPE html>
<html lang="en">
<head>
<meta charset="utf-8">
<title>Vellora Hair Building Fibers – Pack Front</title>
<link href="https://fonts.googleapis.com/css2?family=Advent+Pro:wght@300;400&display=swap" rel="stylesheet">
<style>
  :root {
    --backdrop: #f51c04;
    --pack: #0b0b0c;
    --pack-edge: #1a1a1c;
    --ink: #ffffff;
    --pattern-tone: rgba(120, 120, 125, 0.18);
  }
  * { margin: 0; padding: 0; box-sizing: border-box; }
  html, body {
    width: 824px;
    height: 1200px;
    overflow: hidden;
  }
  body {
    background: var(--backdrop);
    font-family: "Advent Pro", sans-serif;
    color: var(--ink);
    position: relative;
  }
  .pack-front {
    position: absolute;
    left: 209px;
    top: 216px;
    width: 389px;
    height: 714px;
    background: var(--pack);
    box-shadow: 0 0 0 1px var(--pack-edge);
    overflow: hidden;
  }
  .line-fan-pattern {
    position: absolute;
    inset: 0;
    background:
      radial-gradient(ellipse 70% 45% at 85% 30%, var(--pattern-tone), transparent 70%),
      radial-gradient(ellipse 60% 35% at 45% 85%, var(--pattern-tone), transparent 70%);
  }
  .pack-text {
    position: absolute;
    left: 0;
    width: 100%;
    text-align: center;
    font-weight: 300;
    white-space: nowrap;
  }
  .tagline {
    top: 60px;
    font-size: 31px;
    letter-spacing: 0.2px;
  }
  .brand-name {
    top: 350px;
    font-size: 56px;
    font-weight: 400;
    letter-spacing: 6px;
  }
  .product-line {
    top: 468px;
    font-size: 29px;
  }
  .net-weight {
    top: 676px;
    font-size: 15px;
  }
</style>
</head>
<body>
  <main class="pack-front">
    <div class="line-fan-pattern" role="img" aria-label="Faint grey fan of fine diagonal lines across the black pack face"></div>
    <p class="pack-text tagline">Instant Fuller &amp; Thicker Hair</p>
    <h1 class="pack-text brand-name">VELLORA</h1>
    <p class="pack-text product-line">Natural Hair Building Fibers</p>
    <p class="pack-text net-weight">Net Weight 28g</p>
  </main>
</body>
</html>
```